Cedar Grove Worship Chapel CG- Theme for 2022

We, Cedar Grove Worship Chapel of Willow Bend, need a design for a 4' x 6' banner that will be placed on two walls in the main sanctuary. The banner is to communicate/advertise the church's theme for 2022, "He Will Make All Things New: A New You - 2022" Revelations 21:5. The design should include our logo and church name. Use the color purple. We have not worshipped in our church building since 2020 due to the COVID pandemic. This banner should be reflective of change, newness as we plan to re-enter the building this spring. Our congregation demographic is 95% African American, 5% Hispanic. Our home base is Tampa, Florida (USA), but we have a large social media following, primarily due to the pandemic.

Target Market(s)

Church members, Ages 1-99; male and female

Industry/Entity Type

Religious

Font styles to use
Serif

Colors
0094D4
00A9DD
6FCCEA
C7EBF8
E9F6FB
00AB8E
00BBA5
67D7C9
C6EFE9
E9F9F6
6B429C
8869AF
B7A5CE
E3DAEB
F3F0F8

Requirements
Must have
• Theme, scripture, church logo and color purple

```html
<!DOCTYPE html>
<html lang="en">
<head>
<meta charset="utf-8">
<title>Cedar Grove Worship Chapel — A New You 2022</title>
<link href="https://fonts.googleapis.com/css2?family=Bebas+Neue&family=Montserrat:wght@300;400;500;600;700;900&display=swap" rel="stylesheet">
<style>
  :root {
    --page: #f1f1f1;
    --purple: #8612cf;
    --purple-deep: #7a0fc2;
    --purple-fade: rgba(134, 18, 207, 0);
    --ink: #050505;
    --white: #ffffff;
    --cream: #f1d9a8;
    --wall: #e9c9a6;
    --wood: #6b2a1c;
    --carpet: #c0306a;
  }
  * { box-sizing: border-box; margin: 0; padding: 0; }
  html, body {
    width: 1200px; height: 1200px; overflow: hidden;
    background: var(--page);
  }
  .banner {
    position: absolute; left: 0; top: 200px;
    width: 1200px; height: 800px;
    background: var(--purple);
    overflow: hidden;
    font-family: "Montserrat", sans-serif;
    color: var(--white);
  }
  .sanctuary-photo {
    position: absolute; left: 560px; top: 0; width: 640px; height: 800px;
    background:
      linear-gradient(90deg, var(--purple) 0%, rgba(134,18,207,0.55) 22%, var(--purple-fade) 50%),
      linear-gradient(180deg, var(--cream) 0%, var(--wall) 38%, var(--wood) 60%, #8a3226 72%, var(--carpet) 100%);
  }
  .dove-photo {
    position: absolute; left: 510px; top: 134px; width: 270px; height: 206px;
    border-radius: 50%;
    background: radial-gradient(ellipse at center, rgba(255,255,255,0.95) 0%, rgba(245,240,250,0.7) 45%, rgba(255,255,255,0) 72%);
  }
  .theme-line {
    position: absolute; left: 62px; top: 52px;
    font-family: "Bebas Neue", sans-serif;
    font-size: 56px; line-height: 1; letter-spacing: 0.005em;
    text-shadow: 0 2px 4px rgba(0,0,0,0.25);
  }
  .theme-new {
    position: absolute; left: 58px; top: 106px;
    font-weight: 300; font-size: 108px; line-height: 1; letter-spacing: 0.02em;
  }
  .theme-you {
    position: absolute; left: 56px; top: 190px;
    font-weight: 900; font-size: 232px; line-height: 1; letter-spacing: -0.05em;
    color: var(--ink);
  }
  .year-tag {
    position: absolute; left: 62px; top: 404px; width: 200px; height: 98px;
    background: var(--white); border-radius: 8px;
    box-shadow: 0 3px 8px rgba(0,0,0,0.25);
    font-family: "Bebas Neue", sans-serif; font-size: 96px; line-height: 98px;
    color: var(--purple-deep); text-align: center; letter-spacing: 0.01em;
  }
  .scripture-tag {
    position: absolute; left: 261px; top: 423px; width: 346px; height: 58px;
    background: var(--ink); border-radius: 0 8px 8px 0;
    font-weight: 700; font-size: 29px; line-height: 58px;
    padding-left: 20px; letter-spacing: 0.01em;
  }
  .church-name {
    position: absolute; left: 68px; top: 550px;
    border-left: 4px solid var(--ink);
    padding-left: 18px;
    font-weight: 600; font-size: 35px; line-height: 42px; letter-spacing: 0.01em;
  }
  .return-note {
    position: absolute; left: 62px; top: 642px;
    font-weight: 400; font-size: 22px; letter-spacing: 0.02em;
  }
  .web-address {
    position: absolute; left: 64px; top: 687px; width: 656px; height: 72px;
    background: var(--ink); border-radius: 10px;
    font-weight: 600; font-size: 38px; line-height: 72px;
    text-align: center; letter-spacing: 0.1em;
  }
  .church-mark {
    position: absolute; left: 838px; top: 401px; width: 226px; height: 226px;
    border-radius: 50%; background: var(--ink);
    display: flex; align-items: center; justify-content: center;
    font-weight: 600; font-size: 30px; line-height: 36px;
    text-align: center; color: var(--white);
  }
</style>
</head>
<body>
  <main class="banner">
    <div class="sanctuary-photo" role="img" aria-label="Photo of a church sanctuary with wooden pews, stained glass windows, a cross and a red carpeted aisle"></div>
    <div class="theme-line">He Will Make All Things New</div>
    <div class="theme-new">A NEW</div>
    <div class="theme-you">YOU</div>
    <div class="dove-photo" role="img" aria-label="Photo of a white dove in flight"></div>
    <div class="year-tag">2022</div>
    <div class="scripture-tag">Revelations 21:5</div>
    <h1 class="church-name">Cedar Grove Worship Chapel<br>of Willow Bend</h1>
    <p class="return-note">We plan to re-enter the building this spring</p>
    <div class="web-address">www.cedargrovechapel.org</div>
    <div class="church-mark">Cedar<br>Grove</div>
  </main>
</body>
</html>
```